Full Page Marlow 50 Ad

We need a full page magazine ad. Our company is a site construction company - meaning we build lakes, ponds, do brush clearing for farmers and ranchers. For commercial customers, we build building pads, site clearing, pavement and soil stabilization. The final design should show what we do. Our website is www.dunrockgraders.com

```html
<!DOCTYPE html>
<html lang="en">
<head>
<meta charset="utf-8">
<title>Marlow 50 — Dunrock Graders Ad</title>
<link href="https://fonts.googleapis.com/css2?family=Roboto:wght@400;500;700&display=swap" rel="stylesheet">
<style>
  :root {
    --ink: #231f20;
    --band: #2a2627;
    --yellow: #f6b21b;
    --white: #ffffff;
    --sky-top: #ffffff;
    --sky-pale: #dfe7f0;
    --sky-mid: #bccfe4;
    --sky-low: #c9d4da;
    --haze: #e9dcbc;
    --treeline: #6f6e4e;
    --treeline-dark: #57553f;
    --dirt-light: #b2a38c;
    --dirt: #8d7e6a;
    --dirt-dark: #564b3f;
  }
  * { margin: 0; padding: 0; box-sizing: border-box; }
  html, body { width: 927px; height: 1200px; overflow: hidden; background: var(--white); }
  body { font-family: "Roboto", Arial, sans-serif; color: var(--ink); }
  .ad { position: relative; width: 927px; height: 1200px; overflow: hidden; background: var(--white); }

  .stripes { position: absolute; }
  .stripes-top { top: 0; right: 0; width: 321px; height: 12px; }
  .stripes-bottom { bottom: 0; left: 0; width: 927px; height: 22px; }

  .hero-photo {
    position: absolute; left: 0; top: 260px; width: 927px; height: 800px;
    background:
      radial-gradient(ellipse 60% 14% at 40% 57%, rgba(240,226,190,0.7), rgba(240,226,190,0) 100%),
      radial-gradient(ellipse 70% 18% at 55% 78%, rgba(196,182,160,0.55), rgba(196,182,160,0) 100%),
      linear-gradient(180deg,
        var(--sky-top) 0%,
        var(--sky-pale) 8%,
        var(--sky-mid) 24%,
        var(--sky-low) 42%,
        var(--haze) 51%,
        var(--treeline) 55%,
        var(--treeline-dark) 59%,
        var(--dirt-light) 64%,
        var(--dirt) 78%,
        var(--dirt-dark) 100%);
  }

  .brand { position: absolute; left: 58px; top: 118px; display: flex; align-items: center; gap: 12px; }
  .brand-mark { width: 22px; height: 22px; background: var(--yellow); }
  .brand-name { font-size: 34px; font-weight: 700; color: var(--ink); letter-spacing: 0.5px; line-height: 1; }

  .contact { position: absolute; left: 580px; top: 82px; width: 290px; }
  .contact-label { font-size: 14px; font-weight: 500; letter-spacing: 3.5px; text-align: center; margin-left: 10px; }
  .contact-phone { position: absolute; top: 28px; left: 0; width: 290px; height: 48px; }
  .contact-phone-text { position: absolute; left: 66px; top: 11px; font-size: 21px; font-weight: 700; color: var(--white); display: flex; align-items: center; gap: 8px; }

  .headline {
    position: absolute; left: 54px; top: 294px; width: 440px;
    font-size: 42px; font-weight: 500; line-height: 57px; color: var(--ink);
  }

  .services { position: absolute; left: 585px; top: 302px; width: 320px; }
  .services-title { font-size: 26px; font-weight: 500; margin-bottom: 20px; }
  .service-name { font-size: 18px; font-weight: 500; text-transform: uppercase; }
  .service-rule { width: 150px; height: 5px; background: var(--yellow); margin: 8px 0 20px; }
  .service-text { font-size: 16px; line-height: 23px; margin-bottom: 28px; }

  .gallery { position: absolute; left: 53px; top: 915px; display: flex; z-index: 2; }
  .gallery-item { height: 179px; }
  .gallery-grader { width: 189px; background: linear-gradient(160deg, #8a8c8f, #c9a62a 45%, #6f6a62); }
  .gallery-aerial { width: 193px; background: linear-gradient(160deg, #5d7a5c, #9fae98 50%, #4e6650); }
  .gallery-pond { width: 189px; background: linear-gradient(180deg, #dfe6ec 0%, #8c8f62 40%, #7fa04c 65%, #5f7a6e 100%); }

  .footer { position: absolute; left: 0; top: 1060px; width: 927px; height: 118px; background: var(--band); color: var(--white); }
  .footer-links { position: absolute; left: 55px; top: 64px; display: flex; gap: 28px; font-size: 17px; }
  .footer-link { display: flex; align-items: center; gap: 10px; }
  .experience { position: absolute; left: 672px; top: 28px; text-align: center; width: 216px; }
  .experience-years { font-size: 24px; font-weight: 400; }
  .experience-sub { font-size: 14px; letter-spacing: 2.5px; margin-top: 2px; }
  .experience-rule { position: absolute; right: 0; top: 96px; width: 140px; height: 14px; background: var(--yellow); clip-path: polygon(10% 0, 100% 0, 100% 100%, 0 100%); }
</style>
</head>
<body>
<main class="ad">
  <svg class="stripes stripes-top" viewBox="0 0 321 12" aria-hidden="true">
    <polygon points="0,0 150,0 144,12 0,12" fill="var(--ink)"/>
    <polygon points="158,0 196,0 190,12 152,12" fill="var(--yellow)"/>
    <polygon points="204,0 236,0 230,12 198,12" fill="var(--ink)"/>
    <polygon points="244,0 282,0 276,12 238,12" fill="var(--yellow)"/>
    <polygon points="290,0 321,0 321,12 284,12" fill="var(--ink)"/>
  </svg>

  <div class="hero-photo" role="img" aria-label="Photo of a tractor pulling an earth scraper across a freshly graded pond site, tracked dirt slopes in front and oak trees along the horizon"></div>

  <div class="brand">
    <span class="brand-mark"></span>
    <span class="brand-name">Dunrock Graders</span>
  </div>

  <div class="contact">
    <p class="contact-label">CONTACT US AT</p>
    <div class="contact-phone">
      <svg width="290" height="48" viewBox="0 0 290 48" aria-hidden="true">
        <polygon points="0,48 14,0 26,0 12,48" fill="var(--yellow)"/>
        <polygon points="20,48 34,0 46,0 32,48" fill="var(--yellow)"/>
        <polygon points="56,48 70,0 250,0 236,48" fill="var(--ink)"/>
        <polygon points="246,48 260,0 274,0 260,48" fill="var(--yellow)"/>
      </svg>
      <span class="contact-phone-text">
        <svg width="18" height="18" viewBox="0 0 24 24" aria-hidden="true"><path d="M6.6 10.8a15 15 0 0 0 6.6 6.6l2.2-2.2a1 1 0 0 1 1-.25 11.4 11.4 0 0 0 3.6.6 1 1 0 0 1 1 1V20a1 1 0 0 1-1 1A17 17 0 0 1 3 4a1 1 0 0 1 1-1h3.5a1 1 0 0 1 1 1 11.4 11.4 0 0 0 .6 3.6 1 1 0 0 1-.25 1z" fill="none" stroke="var(--yellow)" stroke-width="2"/></svg>
        555-014-2663
      </span>
    </div>
  </div>

  <h1 class="headline">Helping you<br>develop your land<br>for your long or<br>short term goals.</h1>

  <section class="services">
    <h2 class="services-title">What We Do</h2>
    <h3 class="service-name">Residential Services</h3>
    <div class="service-rule"></div>
    <p class="service-text">we build lakes, ponds, brush clearing<br>for farmers and ranchers</p>
    <h3 class="service-name">Commercial Services</h3>
    <div class="service-rule"></div>
    <p class="service-text">we build building pads, site clearing,<br>pavement and soil stabilization</p>
  </section>

  <div class="gallery">
    <div class="gallery-item gallery-grader" role="img" aria-label="Close-up photo of a yellow earth scraper on a dirt site"></div>
    <div class="gallery-item gallery-aerial" role="img" aria-label="Aerial photo of cleared land and wooded lots"></div>
    <div class="gallery-item gallery-pond" role="img" aria-label="Photo of a finished pond with grassy banks and a barn"></div>
  </div>

  <footer class="footer">
    <div class="footer-links">
      <span class="footer-link">
        <svg width="18" height="18" viewBox="0 0 24 24" aria-hidden="true"><g fill="none" stroke="var(--yellow)" stroke-width="2"><circle cx="12" cy="12" r="10"/><ellipse cx="12" cy="12" rx="4.5" ry="10"/><path d="M2 12h20M4 7h16M4 17h16"/></g></svg>
        www.dunrockgraders.com
      </span>
      <span class="footer-link">
        <svg width="18" height="18" viewBox="0 0 24 24" aria-hidden="true"><path d="M6.6 10.8a15 15 0 0 0 6.6 6.6l2.2-2.2a1 1 0 0 1 1-.25 11.4 11.4 0 0 0 3.6.6 1 1 0 0 1 1 1V20a1 1 0 0 1-1 1A17 17 0 0 1 3 4a1 1 0 0 1 1-1h3.5a1 1 0 0 1 1 1 11.4 11.4 0 0 0 .6 3.6 1 1 0 0 1-.25 1z" fill="none" stroke="var(--yellow)" stroke-width="2"/></svg>
        555-014-2663
      </span>
    </div>
    <div class="experience">
      <p class="experience-years">Over 50 Years</p>
      <p class="experience-sub">OF EXPERIENCE</p>
    </div>
    <div class="experience-rule"></div>
  </footer>

  <svg class="stripes stripes-bottom" viewBox="0 0 927 22" aria-hidden="true">
    <rect x="0" y="0" width="927" height="22" fill="var(--white)"/>
    <polygon points="0,0 30,0 22,22 0,22" fill="var(--yellow)"/>
    <polygon points="38,0 110,0 102,22 30,22" fill="var(--ink)"/>
    <polygon points="118,0 150,0 142,22 110,22" fill="var(--yellow)"/>
    <polygon points="158,0 340,0 332,22 150,22" fill="var(--ink)"/>
    <polygon points="348,0 380,0 372,22 340,22" fill="var(--yellow)"/>
    <polygon points="388,0 620,0 612,22 380,22" fill="var(--ink)"/>
    <polygon points="628,0 700,0 692,22 620,22" fill="var(--yellow)"/>
    <polygon points="708,0 927,0 927,22 700,22" fill="var(--ink)"/>
  </svg>
</main>
</body>
</html>
```